Lantern - Web Design Project

We are seeking to have our website redesigned. Our current webpage is rather dated looking www.lantern-outcomes.com We will be utilizing similar content to explain our services as what is in the website now. We do not see it at a retail portal but rather a website for those inquiring about our services as a reference check so to speak.

We wish to have a look that is considered clean, fresh, contemporary and contains a business savvy vibe.

We prefer isolated white background and also wish to retain the integrity of our Logo and colour scheme.

We are looking for something that doesnt look like it was designed at home on sitemoose. We are hoping to find something that looks like it would reside on a tablet.
Updates

Hello designers!

We apologize for our tardiness as we have been quite preoccupied. We will be extending our invites to the end of January!

Hello All,

Please review our offer once again for updated requirements.  We are hoping to accept a design by months end.

Lantern

Target Market(s)

Business to business clients and Large manufacturers

Industry/Entity Type

Retail

Requirements
Must have
• Existing Logo

There must be an area dedicated to an intro video that will be incorporated on our landing page.

We require design of the other pages as well not only the landing page.

```html
<!DOCTYPE html>
<html lang="en">
<head>
<meta charset="utf-8">
<title>Lantern Performance Group</title>
<link rel="stylesheet" href="https://fonts.googleapis.com/css2?family=Copse&family=PT+Sans:ital,wght@0,400;0,700;1,400;1,700&display=swap">
<style>
:root{
  --red:#d0101a;
  --red-dark:#a80a12;
  --ink:#333;
  --muted:#555;
  --line:#cfcfcf;
  --paper:#f4f4f4;
  --btn:#4a4646;
  --footer:#3e3e3e;
}
*{box-sizing:border-box;margin:0;padding:0}
html,body{width:960px;height:1200px;overflow:hidden;background:#fff}
body{position:relative;font-family:"PT Sans",sans-serif;color:var(--ink);font-size:10.5px}
.abs{position:absolute}
.serif{font-family:"Copse",serif}

/* header */
.header{left:0;top:0;width:960px;height:101px;background:linear-gradient(#fafafa,#ececec);border-bottom:1px solid #d6d6d6}
.util{right:104px;top:10px;display:flex;align-items:center;gap:8px;font-size:10.5px}
.util .signin{color:var(--red)}
.util .sep{color:#999}
.search{width:154px;height:18px;border:1px solid #bbb;border-radius:3px;background:#fff;display:flex;overflow:hidden}
.search span{flex:1;padding:2px 6px;color:#999;font-style:italic;font-size:10px}
.search i{width:26px;background:var(--red);display:flex;align-items:center;justify-content:center}
.phone{right:104px;top:53px;display:flex;align-items:center;gap:8px;color:var(--red);font-size:22px;font-weight:700;letter-spacing:.5px}
.phone-icon{width:24px;height:24px;background:#555;border-radius:3px;display:flex;align-items:center;justify-content:center}

/* hero */
.hero{left:0;top:101px;width:960px;height:376px;background:radial-gradient(ellipse at 45% 55%,#d9a050 0%,#9a6a35 30%,#4e3a26 65%,#2a221c 100%)}
.logo-panel{left:104px;top:0;width:176px;height:357px;z-index:2}
.logo-panel svg{position:absolute;left:0;top:0}
.brand{left:0;top:36px;width:176px;text-align:center;font-size:30px;color:#555;font-family:"PT Sans",sans-serif}
.brand-dot{display:inline-block;width:8px;height:8px;border-radius:50%;background:var(--red);margin-right:6px;vertical-align:middle}
.nav{left:95px;top:110px;width:193px;z-index:3}
.nav .home{height:34px;background:linear-gradient(#e8202a,#b90c14);color:#fff;font-family:"Copse",serif;font-size:11px;letter-spacing:1px;padding:10px 0 0 31px;box-shadow:0 2px 3px rgba(0,0,0,.3)}
.nav ul{list-style:none;margin-left:31px;width:141px}
.nav li{font-family:"Copse",serif;font-size:10px;color:#333;height:36.3px;line-height:36px;border-bottom:1px dashed #bbb}
.nav li:last-child{border-bottom:none}
.quote{left:424px;top:294px;width:432px;height:109px;background:rgba(25,20,18,.82);border-radius:5px;padding:10px 12px;color:#fff;font-style:italic;font-weight:700;font-size:14px;line-height:22px}
.quote cite{display:block;text-align:right;color:var(--red);font-size:10px;line-height:14px;margin-top:4px;padding-right:8px}
.dots{left:718px;top:420px;display:flex;gap:8px}
.dots span{width:28px;height:28px;border-radius:50%;background:rgba(255,255,255,.3)}
.dots span.on{background:#fff}

/* content */
.paper{left:0;top:477px;width:893px;height:337px;background:var(--paper)}
.news{left:104px;top:486px;width:752px;height:45px}
.news-label{left:40px;top:14px;font-family:"Copse",serif;font-size:14px;color:#666}
.news-title{left:142px;top:9px;font-size:11.5px;font-weight:700;color:#333}
.news-text{left:142px;top:25px;font-size:9.5px;color:#666}
.news-text em{color:var(--red)}
h2{font-family:"Copse",serif;font-weight:400;color:var(--red);font-size:16px}
.welcome-h{left:104px;top:555px}
.how-h{left:618px;top:555px}
.thumb{border:1px solid #ccc;background:#fff;padding:2px}
.thumb div{width:100%;height:100%}
.welcome-img{left:104px;top:588px;width:121px;height:118px}
.welcome-img div{background:linear-gradient(#c9d5dc 0%,#8c9aa2 35%,#4c5358 55%,#3a3f43 100%)}
.welcome-text{left:238px;top:585px;width:352px;font-size:10.5px;line-height:20px;color:var(--muted)}
.btn{background:var(--btn);color:#fff;font-size:10px;padding:0 10px;height:27px;line-height:27px;text-transform:uppercase}
.welcome-btn{left:238px;top:735px}
.video{left:618px;top:589px;width:238px;height:171px}
.video div{position:relative;background:linear-gradient(#3a3a3a 0%,#514a40 45%,#7a4a2e 75%,#3c2a22 100%)}
.video svg{position:absolute;left:95px;top:54px}
.shadow{height:6px;background:radial-gradient(ellipse at 50% 0,rgba(0,0,0,.25),transparent 70%)}

.box{top:790px;width:240px;height:256px;background:#fff;border:1px solid #ddd;box-shadow:0 1px 3px rgba(0,0,0,.12)}
.box h2{position:absolute;left:12px;top:8px}
.box .btn{position:absolute;bottom:10px}
.who{left:104px}
.who .team{position:absolute;left:9px;top:36px;width:221px;height:74px}
.who .team div{background:linear-gradient(90deg,#4a4f5a,#8a8f99 30%,#2c2f38 60%,#6a6e78)}
.who p{position:absolute;left:10px;top:117px;width:222px;font-size:10px;line-height:18.4px;color:var(--muted)}
.who .btn{left:10px}
.what{left:360px}
.what ul{position:absolute;left:16px;top:36px;width:216px;list-style:none}
.what li{height:29px;line-height:26px;border-bottom:1px dashed #ccc;padding-left:19px;position:relative;font-size:10px;color:#444}
.what li:last-child{border:none}
.what li::before{content:"";position:absolute;left:0;top:10px;border-left:5px solid var(--red);border-top:3px solid transparent;border-bottom:3px solid transparent}
.what .btn{left:16px}
.contact{left:616px}
.field{position:absolute;left:12px;width:210px;height:24px;border:1px solid #ccc;background:linear-gradient(#fff,#f0f0f0);padding:5px 10px;font-size:10px;color:#666}
.contact .btn{right:17px}

/* footer */
.footer{left:0;top:1083px;width:960px;height:117px;background:var(--footer);color:#ddd}
.f-brand{left:104px;top:18px;font-size:27px;color:#bbb}
.f-copy{left:104px;top:73px;font-size:9px;line-height:17px;color:#ccc}
.f-copy b{color:var(--red);font-weight:400}
.f-contact{left:405px;top:18px}
.f-contact h3,.f-follow h3{font-family:"Copse",serif;font-weight:400;font-size:13px;color:#eee}
.f-contact p{font-size:9px;line-height:14.4px;color:#ddd}
.f-contact .co{color:var(--red);font-size:10px;font-weight:700}
.f-follow{left:700px;top:18px}
.socials{display:flex;gap:8px;margin-top:14px}
.socials span{width:24px;height:24px;border-radius:3px;background:#8a8a8a}
</style>
</head>
<body>

<header class="abs header">
  <div class="abs util"><span class="signin">SIGN IN</span><span class="sep">|</span><span>Français</span>
    <div class="search"><span>Search...</span><i><svg width="12" height="12" viewBox="0 0 12 12"><circle cx="4.5" cy="4.5" r="3.2" fill="none" stroke="#fff" stroke-width="1.6"/><line x1="7" y1="7" x2="11" y2="11" stroke="#fff" stroke-width="2"/></svg></i></div>
  </div>
  <div class="abs phone"><span class="phone-icon"><svg width="14" height="16" viewBox="0 0 14 16"><path d="M3 1 L6 1 L6 5 L4 6 Q5 10 8 11 L9 9 L13 10 L13 14 Q6 15 3 9 Q1 5 3 1Z" fill="#fff"/></svg></span>+1.800.555.0147</div>
</header>

<section class="abs hero" role="img" aria-label="Photo of a lit arch bridge leading into a city skyline at dusk"></section>

<div class="abs logo-panel">
  <svg width="176" height="357" viewBox="0 0 176 357"><path d="M0 0 H176 V345 L88 318 L0 345 Z" fill="#fafafa"/></svg>
  <div class="abs brand"><span class="brand-dot"></span>Lantern</div>
</div>

<nav class="abs nav">
  <div class="home">HOME</div>
  <ul>
    <li>WHO WE ARE</li>
    <li>CROSS THE LANTERN</li>
    <li>PERFORMANCE SOLUTIONS</li>
    <li>SUSTAIN SOLUTIONS</li>
    <li>JOIN US</li>
  </ul>
</nav>

<blockquote class="abs quote">"There are managers so preoccupied with their e-mail messages that they never look up from their screens to see what's happening in the nondigital world."<cite>Miriam Castellane</cite></blockquote>
<div class="abs dots"><span class="on"></span><span></span><span></span><span></span></div>

<div class="abs paper"></div>

<div class="abs news">
  <svg class="abs" width="752" height="52" viewBox="0 0 752 52"><path d="M0 0 H752 L730 22 L752 45 H0 L22 22 Z" fill="#fff" stroke="#ddd"/><ellipse cx="376" cy="47" rx="340" ry="3" fill="rgba(0,0,0,.12)"/></svg>
  <span class="abs news-label">Latest News :</span>
  <span class="abs news-title">Lorem ipsum dolor sit amet.</span>
  <span class="abs news-text">Aliquam molestie, mi et imperdiet euismod, dui purus auctor tellus, et interdum lacus....<em>Read More</em></span>
</div>

<h2 class="abs welcome-h">Welcome to Lantern Performance Group</h2>
<div class="abs thumb welcome-img"><div role="img" aria-label="Photo of a coastal road curving along the sea"></div></div>
<p class="abs welcome-text">Lantern Performance Group Inc. is the leading provider of profit generating and people development solutions. With the hands-on experience of best practices, the state-of-the-art technology and in-depth information we help companies increase their efficiencies and profits. Frank, honest, committed, valuable and rewarding are words that customers use to describe the quality services provided by Lantern Performance Group.</p>
<div class="abs btn welcome-btn">Read More</div>

<h2 class="abs how-h">How it Works</h2>
<div class="abs thumb video">
  <div role="img" aria-label="Intro video still of a highway at night with light trails">
    <svg width="46" height="46" viewBox="0 0 46 46"><circle cx="23" cy="23" r="22" fill="rgba(255,255,255,.65)"/><path d="M17 12 L34 23 L17 34 Z" fill="#3a3a3a"/></svg>
  </div>
  <div class="shadow"></div>
</div>

<section class="abs box who">
  <h2>Who We Are ?</h2>
  <div class="thumb team"><div role="img" aria-label="Photo of a business team"></div></div>
  <p>With highly experienced performance consultants, trainers and subject matter experts based throughout the North America, Europe, the Middle East and Asia Pacific we offer unrivalled skills and expertise in designing ...</p>
  <div class="btn">Read More</div>
</section>

<section class="abs box what">
  <h2>What We Do ?</h2>
  <ul>
    <li>Business Diagnostics</li>
    <li>Executive Coaching</li>
    <li>Management Development</li>
    <li>Talent Management</li>
    <li>Creating Sales Culture</li>
    <li>Creating Customer Loyalty</li>
  </ul>
  <div class="btn">Read More</div>
</section>

<section class="abs box contact">
  <h2>Quick Contact</h2>
  <div class="field" style="top:39px">Name</div>
  <div class="field" style="top:69px">Email Address</div>
  <div class="field" style="top:98px">Phone Number</div>
  <div class="field" style="top:128px;height:76px">Your comments</div>
  <div class="btn">Submit Now</div>
</section>

<footer class="abs footer">
  <div class="abs f-brand">Lantern</div>
  <div class="abs f-copy">© Copyright 2013. <b>Lantern Performance Group</b> .<br>All rights reserved</div>
  <div class="abs f-contact">
    <h3>Contact Us</h3>
    <p class="co">Lantern Performance Group</p>
    <p>48 Harbourline Ave, Fernwood,<br>ON K0L 2Q9, Canada<br><b>Phone :</b> +1.800.555.0147<br><b>Email:</b> info@lantern-outcomes.com</p>
  </div>
  <div class="abs f-follow">
    <h3>Follow Us On</h3>
    <div class="socials" aria-label="Social network links"><span></span><span></span><span></span><span></span><span></span></div>
  </div>
</footer>

</body>
</html>
```